Vexo, Extreme Motocross and Downhill Mountain bike. Need Backdrop image involving existing logo

I have just about to kick off a new brand and we are in need of a background image to support our social media pages and website. Our product is apparel for the sports racing, competition and free riding. I wish this to involve images of motocross riders and Mountain bike riders or attributes to combine the sports like helmets, bike parts etc. These images could have the background of mountain trails or motocross tracks for the support. I have added a few websites below to help cover the sports and ideas I am after.

https://www.tarnwolf.com/au-en/event-series/tarnwolf-cliffdrop
https://duneracerleague.com/
https://www.arenadirtcup.com/

I have added my logo below to help with colours and designs. I would like some extra bold text within the design to help support our new brand with great style designs.

```html
<!DOCTYPE html>
<html lang="en">
<head>
<meta charset="utf-8">
<title>Vexo — Backdrop</title>
<link rel="stylesheet" href="https://fonts.googleapis.com/css2?family=Poppins:ital,wght@0,800;1,800&display=swap">
<style>
  :root {
    --brand-red: #e41e1e;
    --stripe-red: #c2181a;
    --white: #ffffff;
    --sky-deep: #0c1620;
    --sky-blue: #2a4356;
    --sky-haze: #4f5e66;
    --dust-glow: #8a6f55;
    --dust-mid: #5e4835;
    --dust-dark: #2b1f15;
    --gear-red: #7a2222;
    --shade: rgba(6, 8, 12, 0.42);
  }
  * { margin: 0; padding: 0; box-sizing: border-box; }
  html, body {
    width: 1200px;
    height: 640px;
    overflow: hidden;
    background: #111;
  }
  .backdrop {
    position: relative;
    width: 1200px;
    height: 640px;
    overflow: hidden;
    font-family: "Poppins", sans-serif;
    color: var(--white);
  }
  .hero-photo {
    position: absolute;
    inset: 0;
    background:
      radial-gradient(ellipse 16% 42% at 66% 44%, rgba(122, 34, 34, 0.75), transparent 72%),
      radial-gradient(ellipse 12% 22% at 74% 78%, rgba(180, 170, 160, 0.35), transparent 70%),
      radial-gradient(ellipse 38% 30% at 22% 52%, rgba(150, 120, 92, 0.8), transparent 72%),
      radial-gradient(ellipse 30% 24% at 88% 66%, rgba(140, 112, 86, 0.55), transparent 72%),
      radial-gradient(ellipse 60% 30% at 50% 98%, rgba(40, 28, 18, 0.9), transparent 75%),
      linear-gradient(180deg, var(--sky-deep) 0%, var(--sky-blue) 30%, var(--sky-haze) 46%, var(--dust-glow) 62%, var(--dust-mid) 80%, var(--dust-dark) 100%);
  }
  .hero-shade {
    position: absolute;
    inset: 0;
    background:
      linear-gradient(90deg, rgba(6, 8, 12, 0.25) 0%, transparent 60%),
      var(--shade);
  }
  .stripes {
    position: absolute;
    display: block;
  }
  .stripes--top {
    top: 0;
    right: 0;
    width: 256px;
    height: 54px;
  }
  .stripes--bottom {
    left: 0;
    bottom: 0;
    width: 152px;
    height: 34px;
  }
  .brand {
    position: absolute;
    left: 94px;
    top: 71px;
    display: flex;
    align-items: flex-end;
    gap: 16px;
  }
  .brand__name {
    font-weight: 800;
    font-size: 140px;
    line-height: 140px;
    letter-spacing: 1px;
    color: var(--white);
  }
  .brand__mark {
    width: 24px;
    height: 24px;
    background: var(--brand-red);
    margin-bottom: 21px;
  }
  .headline {
    position: absolute;
    left: 94px;
    top: 376px;
    font-weight: 800;
    font-style: italic;
    font-size: 61px;
    line-height: 68px;
    letter-spacing: 1px;
    text-transform: uppercase;
    white-space: nowrap;
    color: var(--white);
  }
  .headline__accent { color: var(--brand-red); }
  .headline__chevrons {
    display: inline-block;
    width: 138px;
    height: 44px;
    margin-left: 36px;
    vertical-align: 2px;
  }
</style>
</head>
<body>
  <main class="backdrop">
    <div class="hero-photo" role="img" aria-label="Motocross rider in red gear cornering on a dirt track, throwing up a cloud of dust under a dark blue sky"></div>
    <div class="hero-shade"></div>

    <svg class="stripes stripes--top" viewBox="0 0 256 54" aria-hidden="true">
      <g fill="var(--stripe-red)">
        <polygon points="27,0 59,0 32,54 0,54"/>
        <polygon points="91,0 123,0 96,54 64,54"/>
        <polygon points="155,0 187,0 160,54 128,54"/>
        <polygon points="219,0 256,0 256,4 224,54 192,54"/>
      </g>
    </svg>

    <svg class="stripes stripes--bottom" viewBox="0 0 152 34" aria-hidden="true">
      <g fill="var(--white)">
        <polygon points="15,0 31,0 16,34 0,34"/>
        <polygon points="47,0 63,0 48,34 32,34"/>
        <polygon points="79,0 95,0 80,34 64,34"/>
        <polygon points="111,0 127,0 112,34 96,34"/>
      </g>
    </svg>

    <div class="brand">
      <span class="brand__name">VEXO</span>
      <span class="brand__mark" aria-hidden="true"></span>
    </div>

    <h1 class="headline">
      Lorem ipsum dolor<br>
      sit amet, <span class="headline__accent">consectetur</span><svg class="headline__chevrons" viewBox="0 0 138 44" aria-hidden="true">
        <g fill="var(--white)">
          <polygon points="0,22 36,0 36,44"/>
          <polygon points="51,22 87,0 87,44"/>
          <polygon points="102,22 138,0 138,44"/>
        </g>
      </svg>
    </h1>
  </main>
</body>
</html>
```